TC Fruit Trays / Fruit Basket sign

We are Tansy Corner, a supermarket franchisee. We need a more professional look on some of our in-store signs. I will attach a jpg of an existing sign, and also share a dropbox folder with our current logos.
https://www.filebarn.net/sh/k4pq8zt1mmwe2xr/Qa7T3Hn9Km
Here is a link to our Mr. Bolt character art, but use it sparingly - it looks bad to have too much of it in our graphics:
https://www.filebarn.net/sh/v8cn2jd5ttqu4ly/Rf3KsLe8Xo
In fact, you may choose not to use the character art work, if you feel the design looks more professional. This is the first project we have tried using SketchHive, and have many more sign projects that also need to be done. The winning design choice will get first shot at the remaining design projects. Thanks!
Adults 18+
Store

```html
<!DOCTYPE html>
<html lang="en">
<head>
<meta charset="UTF-8">
<title>Tansy Corner – Fruit Trays and Fruit Baskets</title>
<link rel="stylesheet" href="https://fonts.googleapis.com/css2?family=Roboto+Condensed:wght@300;700&display=swap">
<style>
  :root {
    --brand-red: #d9222a;
    --ink: #111111;
    --paper: #ffffff;
    --leaf-light: #eef6dc;
    --leaf-glow: #d8ec9a;
    --leaf-deep: #a9d070;
    --fruit-orange: #f5a11c;
    --fruit-red: #b8161f;
    --fruit-green: #8cc63f;
    --fruit-yellow: #f8dc6a;
  }

  html, body {
    margin: 0;
    padding: 0;
    overflow: hidden;
    background: var(--paper);
  }

  .sign {
    position: relative;
    width: 1200px;
    height: 449px;
    overflow: hidden;
    font-family: "Roboto Condensed", "Arial Narrow", sans-serif;
    background:
      radial-gradient(circle at 86% 20%, rgba(255,255,230,0.95) 0, rgba(255,255,230,0) 28%),
      radial-gradient(circle at 96% 85%, var(--leaf-glow) 0, rgba(216,236,154,0) 40%),
      linear-gradient(90deg, var(--paper) 0%, var(--paper) 42%, var(--leaf-light) 62%, var(--leaf-glow) 82%, var(--leaf-deep) 100%);
  }

  .fruit-photo {
    position: absolute;
    left: 0;
    top: 0;
    width: 840px;
    height: 449px;
    background:
      radial-gradient(ellipse at 16% 86%, var(--fruit-orange) 0, rgba(245,161,28,0) 30%),
      radial-gradient(ellipse at 53% 34%, var(--fruit-red) 0, rgba(184,22,31,0) 22%),
      radial-gradient(ellipse at 40% 66%, var(--fruit-green) 0, rgba(140,198,63,0) 26%),
      radial-gradient(ellipse at 70% 18%, var(--fruit-orange) 0, rgba(245,161,28,0) 18%),
      radial-gradient(ellipse at 66% 60%, var(--fruit-green) 0, rgba(140,198,63,0) 16%),
      radial-gradient(ellipse at 28% 50%, var(--fruit-yellow) 0, rgba(248,220,106,0) 20%);
  }

  .brand {
    position: absolute;
    left: 34px;
    top: 58px;
    display: flex;
    align-items: center;
    gap: 14px;
  }

  .brand-dot {
    width: 60px;
    height: 60px;
    border-radius: 50%;
    background: var(--brand-red);
  }

  .brand-name {
    font-weight: 700;
    font-size: 32px;
    color: var(--ink);
    letter-spacing: 0.5px;
  }

  .headline {
    position: absolute;
    right: 43px;
    top: 118px;
    margin: 0;
    text-align: right;
    color: var(--brand-red);
  }

  .headline-lead {
    display: block;
    font-weight: 700;
    font-size: 86px;
    line-height: 0.82;
    letter-spacing: -0.5px;
  }

  .headline-offer {
    display: block;
    margin-top: 22px;
    font-weight: 300;
    font-size: 52px;
    line-height: 0.98;
    text-align: left;
    letter-spacing: 0.5px;
  }
</style>
</head>
<body>
  <main class="sign">
    <div class="fruit-photo" role="img" aria-label="Photograph of fresh cut fruit: orange halves, red and green apples, pineapple chunks, lime and strawberries"></div>

    <div class="brand">
      <span class="brand-dot" aria-hidden="true"></span>
      <span class="brand-name">Tansy Corner</span>
    </div>

    <h1 class="headline">
      <span class="headline-lead">WE<br>MAKE</span>
      <span class="headline-offer">FRUITS TRAYS OR<br>FRUIT BASKETS</span>
    </h1>
  </main>
</body>
</html>
```